Brand new website for global research and investment startup

We need a simple website, maybe 3 pages: landing page with business description, investment philosophy, team and contact info.
We have a logo already that can be incorporated. Please use the logo only, not the text
We like the color green, something along the lines of #3D6C32 as the main color.
We'd like to design the website with geometric shapes in gradations of the base color. The shapes should suggest "work in progress", "built to last (a long time)", "solidity" and "indestructibility". One idea floating in my head sees smaller features with icosahedron and dodecahedron shapes, and maybe larger structures like crystal lattices; but please feel free to be creative and imagine your own.

```html
<!DOCTYPE html>
<html lang="en">
<head>
<meta charset="utf-8">
<title>Aldmoor Partners — Website Design</title>
<link href="https://fonts.googleapis.com/css2?family=Inter:wght@300;400;500;600&display=swap" rel="stylesheet">
<style>
:root{
  --board:#3e6e33;
  --green:#3d6c32;
  --green-mid:#5b8a4f;
  --green-soft:#a9c3a0;
  --paper:#faf9f6;
  --band:#f1f0eb;
  --ink:#1b1b1b;
  --muted:#5f5f5f;
  --soft:#8a8a8a;
  --line:#e4e2dc;
  --dark:#141414;
  --card:#1d1d1d;
  --card-line:#3a3a3a;
  --ghost:#e2e1dd;
}
*{margin:0;padding:0;box-sizing:border-box}
html,body{width:1035px;height:1200px;overflow:hidden;background:#fff;font-family:'Inter',sans-serif;color:var(--ink)}
.board{position:absolute;left:9px;top:9px;width:1015px;height:1180px;background:var(--board)}
.board-tag{position:absolute;left:9px;top:1px;font-size:2.6px;background:var(--green);color:#fff;padding:1px 3px}
.page{position:absolute;top:31px;width:318px;background:var(--paper);overflow:hidden}
.page > *{position:absolute}
.brand{font-size:6px;font-weight:500;letter-spacing:.2px;color:var(--ink);display:flex;align-items:center;gap:2.5px}
.brand::before{content:"";width:5px;height:5px;background:var(--green)}
.brand.light{color:#fff}
.brand.light::before{background:#fff}
.brand-ghost{font-size:26px;font-weight:500;color:var(--ghost);letter-spacing:-.5px}
.nav-link{font-size:3.4px;color:var(--ink);top:9px}
.nav-link.active{color:var(--green);font-weight:500}
.nav-btn{top:6px;width:28px;height:8px;border:.5px solid var(--green);color:var(--green);font-size:2.8px;display:flex;align-items:center;justify-content:center}
.eyebrow{font-size:2.4px;font-weight:600;color:var(--green);letter-spacing:.2px;text-transform:uppercase}
.display{font-size:18.5px;font-weight:300;line-height:1.05;letter-spacing:-.2px;color:var(--ink)}
.h2{font-size:11px;font-weight:300;line-height:1.15}
.h3{font-size:12.5px;font-weight:300;line-height:1.1}
.body{font-size:4.3px;line-height:7px;color:var(--muted)}
.small{font-size:3.2px;line-height:5.6px;color:var(--muted)}
.rule{height:.5px;background:var(--line)}
.btn{height:9px;display:flex;align-items:center;justify-content:center;font-size:2.8px;color:#fff}
.btn.green{background:var(--green)}
.btn.black{background:var(--dark)}
.text-link{font-size:2.9px;color:var(--green)}
.photo{display:block}
.dark-band{left:0;background:var(--dark);width:318px}
.principle-card{width:90px;height:42px;background:var(--card);padding:8px 7px}
.principle-card.active{border:.5px solid var(--card-line)}
.principle-card .num{font-size:3.6px;color:var(--green);display:block}
.principle-card .ttl{font-size:4.3px;color:#fff;display:block;margin-top:6px}
.principle-card .dsc{font-size:2.6px;line-height:4.3px;color:#6f6f6f;display:block;margin-top:2px}
.leader-name{font-size:4.8px;color:var(--ink)}
.leader-role{font-size:2.6px;color:var(--green)}
.leader-bio{font-size:2.9px;line-height:4.8px;color:var(--muted);width:88px}
.field-label{font-size:2.3px;color:var(--soft);letter-spacing:.2px;text-transform:uppercase}
.field-value{font-size:3.5px;line-height:5px;color:var(--ink);font-weight:500}
.footer{left:0;width:318px;height:50px;background:var(--dark)}
.footer .brand{position:absolute;left:18px;top:16px}
.footer .copy{position:absolute;left:18px;top:30px;font-size:2.6px;color:#7c7c7c}
.footer .links{position:absolute;right:18px;top:30px;display:flex;gap:9px;font-size:2.6px;color:#7c7c7c}
.tenet-num{font-size:3.6px;color:var(--green);font-weight:500}
.tenet-title{font-size:7px;font-weight:400;color:var(--ink)}
.tenet-body{font-size:3.4px;line-height:6px;color:var(--muted)}
.tenet-icon{width:14px;height:14px;stroke:var(--green);fill:none;stroke-width:1}
.step-dot{width:8px;height:8px;border-radius:50%;background:var(--green);color:#fff;font-size:2.4px;display:flex;align-items:center;justify-content:center}
.step-line{height:.5px;background:#cfcdc6;width:38px}
.step-title{font-size:3.8px;font-weight:600;color:var(--ink)}
.step-body{font-size:2.7px;line-height:4.3px;color:var(--muted);width:48px}
.member-name{font-size:8px;font-weight:300;color:var(--ink)}
.member-role{font-size:2.5px;color:var(--green);font-weight:600;letter-spacing:.15px}
.member-bio{font-size:3.1px;line-height:5.6px;color:var(--muted);width:155px}
.input{width:124px;height:10px;background:#fff;border:.5px solid var(--line);font-size:2.8px;color:#aaa;padding:3px 4px}
.form-label{font-size:2.4px;font-weight:600;color:var(--ink)}
</style>
</head>
<body>
<div class="board"></div>
<div class="board-tag">Aldmoor Partners UI design</div>

<!-- Landing page -->
<section class="page" style="left:31px;height:1090px;">
  <div class="brand" style="left:18px;top:7px;">Aldmoor</div>
  <span class="nav-link" style="left:209px;">Philosophy</span>
  <span class="nav-link" style="left:235px;">Team</span>
  <span class="nav-link" style="left:250px;">Contact</span>
  <span class="nav-btn" style="left:272px;">Get in Touch</span>

  <div class="photo" role="img" aria-label="Portrait of a senior partner seated at a desk with a laptop" style="left:163px;top:20px;width:155px;height:158px;background:linear-gradient(90deg,#faf9f6 0%,#efeeea 30%,#d6d5d1 55%,#3b3e46 78%,#e2e2e0 100%);"></div>
  <h1 class="display" style="left:18px;top:52px;">Building value<br>that endures.</h1>
  <p class="body" style="left:18px;top:102px;width:135px;">Halden Capital is an institutional investment firm. We partner with market-leading enterprises, structuring permanent capital solutions designed to compound value over generations.</p>
  <span class="btn green" style="left:18px;top:136px;width:45px;">Explore Our Approach</span>
  <span class="text-link" style="left:70px;top:139px;">Read Annual Letter →</span>

  <div class="rule" style="left:18px;top:195px;width:282px;"></div>
  <p style="left:18px;top:209px;width:162px;font-size:7.2px;line-height:10px;font-weight:300;">We invest with a long-term perspective, seeking businesses and opportunities with the structural qualities to compound value over time.</p>
  <p class="small" style="left:188px;top:210px;width:112px;">Our strategy avoids short-term momentum in favor of fundamental business resilience. By providing permanent capital, we align ourselves fully with management teams to build durable infrastructure, navigate market cycles, and cultivate compound growth.</p>
  <p class="small" style="left:188px;top:250px;width:112px;">We bring disciplined analytical rigor, robust capital resources, and an active operational advisory network to every core partnership.</p>

  <div class="dark-band" style="top:282px;height:369px;"></div>
  <span class="eyebrow" style="left:18px;top:310px;">Our Philosophy</span>
  <h2 class="h2" style="left:18px;top:318px;color:#fff;">The Principles of Endurance</h2>
  <div class="principle-card active" style="left:18px;top:347px;"><span class="num">01</span><span class="ttl">Long-Term Thinking</span><span class="dsc">Decisions measured in decades, not quarters. Aligning capital with multi-generation outcomes.</span></div>
  <div class="principle-card" style="left:114px;top:347px;"><span class="num">02</span><span class="ttl">Conviction</span><span class="dsc">Concentrated portfolios of high-integrity enterprises we understand deeply.</span></div>
  <div class="principle-card" style="left:210px;top:347px;"><span class="num">03</span><span class="ttl">Discipline</span><span class="dsc">Strict price and process structure. Saying no to good to wait for the exceptional.</span></div>
  <div class="principle-card" style="left:18px;top:393px;"><span class="num">04</span><span class="ttl">Fundamental Value</span><span class="dsc">Investing based on tangible assets, robust margins, and clear cash generation.</span></div>
  <div class="principle-card" style="left:114px;top:393px;"><span class="num">05</span><span class="ttl">Resilience</span><span class="dsc">Capital structures engineered to withstand severe macroeconomic volatility.</span></div>
  <div class="principle-card" style="left:210px;top:393px;"><span class="num">06</span><span class="ttl">Compounding</span><span class="dsc">Reinvesting systematically, harnessing the exponential power of time.</span></div>
  <h3 class="h3" style="left:18px;top:466px;color:#fff;width:200px;">We look for strength beneath<br>the surface.</h3>
  <p class="small" style="left:18px;top:500px;width:182px;color:#7d7d7d;">Just as enduring architecture relies on invisible foundational piles, the strongest enterprises are anchored by deep structural competitive advantages, robust unit economics, and principled governance.</p>
  <div class="photo" role="img" aria-label="Aerial view of a team meeting around sofas on a pale tiled floor" style="left:18px;top:536px;width:282px;height:84px;background:linear-gradient(100deg,#e6e6e3 0%,#d9dad7 45%,#c7c8c4 70%,#dcdcd9 100%);"></div>

  <span class="eyebrow" style="left:18px;top:679px;">Leadership</span>
  <h2 class="h2" style="left:18px;top:687px;">Institutional Stewards</h2>
  <div class="photo" role="img" aria-label="Portrait of Edmund Lowrie" style="left:18px;top:711px;width:88px;height:117px;background:linear-gradient(160deg,#4a4038,#2a2522 60%,#1c1a19);"></div>
  <div class="photo" role="img" aria-label="Portrait of Clara Voss" style="left:115px;top:711px;width:88px;height:117px;background:linear-gradient(160deg,#4a4a48,#333432 60%,#1f1f1f);"></div>
  <div class="photo" role="img" aria-label="Portrait of Marcus Adeyemi" style="left:212px;top:711px;width:88px;height:117px;background:linear-gradient(160deg,#5e6e7a,#3b4d63 55%,#222c3c);"></div>
  <span class="leader-name" style="left:18px;top:834px;">Edmund Lowrie</span>
  <span class="leader-role" style="left:18px;top:841px;">MANAGING PARTNER</span>
  <p class="leader-bio" style="left:18px;top:847px;">Edmund oversees global strategy and capital allocation, bringing over 25 years of institutional private equity stewardship.</p>
  <span class="leader-name" style="left:115px;top:834px;">Clara Voss</span>
  <span class="leader-role" style="left:115px;top:841px;">PARTNER, INVESTMENTS</span>
  <p class="leader-bio" style="left:115px;top:847px;">Clara leads our fundamental underwriting team, identifying compounders across manufacturing and industrial technology sectors.</p>
  <span class="leader-name" style="left:212px;top:834px;">Marcus Adeyemi</span>
  <span class="leader-role" style="left:212px;top:841px;">PARTNER, OPERATIONS</span>
  <p class="leader-bio" style="left:212px;top:847px;">Marcus partners with portfolio CEOs to institutionalize operating frameworks and build scalable, resilient infrastructure.</p>

  <div class="rule" style="left:0;top:894px;width:318px;"></div>
  <h3 class="h3" style="left:18px;top:925px;">Let's build something<br>enduring.</h3>
  <p class="small" style="left:18px;top:957px;width:132px;">Whether you represent an institution seeking resilient alignment or a business looking for permanent capital, we welcome a disciplined conversation.</p>
  <span class="field-label" style="left:18px;top:983px;">Email</span>
  <span class="field-value" style="left:18px;top:987px;">partners@haldencap.example</span>
  <span class="field-label" style="left:76px;top:983px;">Office</span>
  <span class="field-value" style="left:76px;top:987px;font-weight:400;">8 Carrow Yard, London</span>
  <span class="btn black" style="left:18px;top:1003px;width:36px;">Inquire Privately</span>
  <div class="photo" role="img" aria-label="Dark teal render of faceted crystal blocks" style="left:188px;top:923px;width:113px;height:88px;background:linear-gradient(135deg,#0e1a1f 0%,#1f4b55 40%,#0b1418 65%,#3f7d88 100%);"></div>

  <footer class="footer" style="top:1040px;">
    <span class="brand light">Aldmoor</span>
    <span class="copy">© 2026 Aldmoor Partners. All rights reserved.</span>
    <span class="links"><span>Privacy Notice</span><span>Terms of Use</span><span>Regulatory Disclosures</span></span>
  </footer>
</section>

<!-- Philosophy page -->
<section class="page" style="left:358px;height:1135px;">
  <div class="brand" style="left:18px;top:7px;">Aldmoor</div>
  <span class="nav-link active" style="left:209px;">Philosophy</span>
  <span class="nav-link" style="left:235px;">Team</span>
  <span class="nav-link" style="left:250px;">Contact</span>
  <span class="nav-btn" style="left:272px;">Get in Touch</span>

  <span class="brand-ghost" style="left:205px;top:70px;">Aldmoor</span>
  <span class="eyebrow" style="left:17px;top:53px;">Investment Philosophy</span>
  <h1 class="display" style="left:17px;top:61px;">Long-term value is built,<br>not predicted.</h1>
  <p class="body" style="left:17px;top:110px;width:164px;">We reject the ephemeral trends of public markets. Halden Capital structures customized, permanent capital partnerships that empower outstanding businesses to make generational decisions.</p>
  <div class="photo" role="img" aria-label="Overhead view of colleagues talking on a pale tiled floor" style="left:0;top:162px;width:318px;height:120px;background:linear-gradient(110deg,#b99a82 0%,#e3e2de 18%,#d8d8d4 50%,#e6e5e1 100%);"></div>

  <span class="tenet-num" style="left:17px;top:304px;">01</span>
  <span class="tenet-title" style="left:17px;top:315px;">Think Long Term</span>
  <p class="tenet-body" style="left:17px;top:326px;width:145px;">We focus on durable value creation rather than short-term market noise. Our investment horizon is measured in decades, allowing compound growth to work unfettered by artificial quarterly targets.</p>
  <svg class="tenet-icon" style="left:250px;top:314px;" viewBox="0 0 14 14"><path d="M3 1h8M3 13h8M4 1c0 4 6 4 6 6s-6 2-6 6M10 1c0 4-6 4-6 6s6 2 6 6"/></svg>
  <div class="rule" style="left:17px;top:354px;width:283px;"></div>

  <svg class="tenet-icon" style="left:54px;top:386px;" viewBox="0 0 14 14"><path d="M7 1l6 3-6 3-6-3z"/><path d="M1 7l6 3 6-3M1 10l6 3 6-3"/></svg>
  <span class="tenet-num" style="left:150px;top:377px;">02</span>
  <span class="tenet-title" style="left:150px;top:388px;">Seek Structural Strength</span>
  <p class="tenet-body" style="left:150px;top:399px;width:150px;">We look beneath surface performance to understand the fundamentals supporting an opportunity. Strong competitive moats and pricing power matter far more than temporary macroeconomic momentum.</p>
  <div class="rule" style="left:17px;top:427px;width:283px;"></div>

  <span class="tenet-num" style="left:17px;top:449px;">03</span>
  <span class="tenet-title" style="left:17px;top:460px;">Compound with Conviction</span>
  <p class="tenet-body" style="left:17px;top:471px;width:145px;">We prefer a concentrated portfolio of high-quality opportunities where our conviction is strongest. We spend deep analytical resources to understand our partners, favoring depth over breadth.</p>
  <svg class="tenet-icon" style="left:250px;top:458px;" viewBox="0 0 14 14"><path d="M1 10l4-4 3 3 5-5M9 4h4v4"/></svg>
  <div class="rule" style="left:17px;top:499px;width:283px;"></div>

  <svg class="tenet-icon" style="left:54px;top:531px;" viewBox="0 0 14 14"><path d="M7 1l5 2v4c0 3-2 5-5 6-3-1-5-3-5-6V3z"/></svg>
  <span class="tenet-num" style="left:150px;top:521px;">04</span>
  <span class="tenet-title" style="left:150px;top:532px;">Build for Resilience</span>
  <p class="tenet-body" style="left:150px;top:543px;width:150px;">We value businesses capable of navigating changing environments and technological shifts. Antifragility under stress is a primary hallmark of the capital structures we actively design.</p>
  <div class="rule" style="left:17px;top:572px;width:283px;"></div>

  <span class="tenet-num" style="left:17px;top:594px;">05</span>
  <span class="tenet-title" style="left:17px;top:605px;">Exercise Discipline</span>
  <p class="tenet-body" style="left:17px;top:616px;width:145px;">Process over impulse. We maintain strict criteria and exceptional patience. We are entirely comfortable saying no to good opportunities in order to deploy our reserves exclusively into the exceptional.</p>
  <svg class="tenet-icon" style="left:250px;top:603px;" viewBox="0 0 14 14"><circle cx="7" cy="7" r="6"/><path d="M7 1v4M7 9v4M1 7h4M9 7h4"/></svg>
  <div class="rule" style="left:17px;top:644px;width:283px;"></div>

  <svg class="tenet-icon" style="left:54px;top:676px;" viewBox="0 0 14 14"><path d="M7 1v12M4 13h6M2 3h10M2 3l-1.5 5h3zM12 3l-1.5 5h3zM0.5 8a1.5 1 0 0 0 3 0M10.5 8a1.5 1 0 0 0 3 0"/></svg>
  <span class="tenet-num" style="left:150px;top:666px;">06</span>
  <span class="tenet-title" style="left:150px;top:677px;">Invest with Integrity</span>
  <p class="tenet-body" style="left:150px;top:688px;width:150px;">Alignment of interests, transparency, and ethical conduct are non-negotiable foundations of everything we do. We serve as responsible stewards of capital for both our partners and our investors.</p>
  <div class="rule" style="left:17px;top:717px;width:283px;"></div>

  <div class="rule" style="left:0;top:744px;width:318px;"></div>
  <span class="eyebrow" style="left:17px;top:772px;">Our Workflow</span>
  <h2 class="h2" style="left:17px;top:780px;">The Engineering of Capital</h2>
  <span class="step-dot" style="left:17px;top:808px;">I</span><span class="step-line" style="left:29px;top:812px;"></span>
  <span class="step-dot" style="left:76px;top:808px;">II</span><span class="step-line" style="left:88px;top:812px;"></span>
  <span class="step-dot" style="left:135px;top:808px;">III</span><span class="step-line" style="left:147px;top:812px;"></span>
  <span class="step-dot" style="left:194px;top:808px;">IV</span><span class="step-line" style="left:206px;top:812px;"></span>
  <span class="step-dot" style="left:253px;top:808px;">V</span>
  <span class="step-title" style="left:17px;top:821px;">Understand</span>
  <p class="step-body" style="left:17px;top:828px;">Immersive research into market structure, competitive dynamics, and operating realities.</p>
  <span class="step-title" style="left:76px;top:821px;">Evaluate</span>
  <p class="step-body" style="left:76px;top:828px;">Rigorous underwriting focused on margin sustainability and true asset-level resilience.</p>
  <span class="step-title" style="left:135px;top:821px;">Commit</span>
  <p class="step-body" style="left:135px;top:828px;">Deployment of permanent, structured capital matched exactly to company horizons.</p>
  <span class="step-title" style="left:194px;top:821px;">Build</span>
  <p class="step-body" style="left:194px;top:828px;">Active operational advisory partnership to scale durable internal infrastructure.</p>
  <span class="step-title" style="left:253px;top:821px;">Compound</span>
  <p class="step-body" style="left:253px;top:828px;">Systematic reinvestment and compounding of generational enterprise value.</p>
  <div class="rule" style="left:0;top:871px;width:318px;"></div>

  <h3 class="h3" style="left:17px;top:900px;">Strong foundations create<br>lasting value.</h3>
  <p class="small" style="left:17px;top:935px;width:182px;">We invite inquiries from institutional asset allocators and exceptional management teams who share our commitment to long-term discipline.</p>
  <div class="photo" role="img" aria-label="Dark field of geometric blocks with one glowing green cube" style="left:17px;top:966px;width:283px;height:62px;border-radius:2px;background:radial-gradient(ellipse 30px 22px at 68% 48%,#4dff5a 0%,#1f8a2c 45%,transparent 100%),linear-gradient(100deg,#102027 0%,#1d3640 50%,#0d1a20 100%);"></div>
  <span class="btn black" style="left:17px;top:1046px;width:31px;">Get in Touch</span>
  <span class="text-link" style="left:55px;top:1049px;">Read Our Investment Letters →</span>

  <footer class="footer" style="top:1086px;">
    <span class="brand light">Aldmoor</span>
    <span class="copy">© 2026 Aldmoor Partners. All rights reserved.</span>
    <span class="links"><span>Privacy Notice</span><span>Terms of Use</span><span>Regulatory Disclosures</span></span>
  </footer>
</section>

<!-- Team page -->
<section class="page" style="left:684px;height:884px;">
  <div class="brand" style="left:18px;top:7px;">Aldmoor</div>
  <span class="nav-link" style="left:209px;">Philosophy</span>
  <span class="nav-link active" style="left:235px;">Team</span>
  <span class="nav-link" style="left:250px;">Contact</span>
  <span class="nav-btn" style="left:272px;">Get in Touch</span>

  <span class="eyebrow" style="left:17px;top:53px;">Our Team</span>
  <h1 class="display" style="left:17px;top:61px;">People of conviction.</h1>
  <p class="body" style="left:17px;top:90px;width:165px;">A small, experienced team united by shared principles and long-term thinking.</p>
  <div class="rule" style="left:0;top:127px;width:318px;"></div>

  <div class="photo" role="img" aria-label="Portrait of Edmund Lowrie" style="left:17px;top:149px;width:110px;height:132px;background:linear-gradient(160deg,#4a4038,#2a2522 60%,#1c1a19);"></div>
  <span class="member-name" style="left:146px;top:186px;">Edmund Lowrie</span>
  <span class="member-role" style="left:146px;top:197px;">MANAGING PARTNER</span>
  <p class="member-bio" style="left:146px;top:204px;">Edmund founded Halden Capital in 2008 with a conviction that patient, disciplined capital allocation creates enduring value. With over 25 years of experience spanning private equity, public markets, and real assets, he leads the firm's investment strategy and portfolio construction.</p>
  <p class="member-bio" style="left:146px;top:234px;">Prior to Halden, Edmund was a Partner at Granite Row and began his career at Whitcombe &amp; Co.</p>
  <div class="rule" style="left:0;top:304px;width:318px;"></div>

  <div class="photo" role="img" aria-label="Portrait of Clara Voss" style="left:190px;top:325px;width:110px;height:132px;background:linear-gradient(160deg,#4a4a48,#333432 60%,#1f1f1f);"></div>
  <span class="member-name" style="left:17px;top:365px;">Clara Voss</span>
  <span class="member-role" style="left:17px;top:376px;">PARTNER — INVESTMENTS</span>
  <p class="member-bio" style="left:17px;top:383px;">Clara leads investment research and due diligence across all strategies. Her background in structural engineering informs her analytical approach — she evaluates investments the way an engineer evaluates load-bearing structures.</p>
  <p class="member-bio" style="left:17px;top:407px;">She joined Halden in 2012 from Harbourline Advisors, where she managed a concentrated global equity portfolio.</p>
  <div class="rule" style="left:0;top:480px;width:318px;"></div>

  <div class="photo" role="img" aria-label="Portrait of Marcus Adeyemi" style="left:17px;top:502px;width:110px;height:132px;background:linear-gradient(160deg,#5e6e7a,#3b4d63 55%,#222c3c);"></div>
  <span class="member-name" style="left:146px;top:545px;">Marcus Adeyemi</span>
  <span class="member-role" style="left:146px;top:556px;">PARTNER — OPERATIONS</span>
  <p class="member-bio" style="left:146px;top:563px;">Marcus oversees portfolio operations, risk management, and investor relations. His focus is ensuring that operational excellence supports long-term value creation across every investment.</p>
  <p class="member-bio" style="left:146px;top:585px;">Before joining Halden in 2014, Marcus held senior roles at Corbel Holdings and Ashby Consulting.</p>

  <div style="left:0;top:656px;width:318px;height:179px;background:var(--band);"></div>
  <span class="eyebrow" style="left:17px;top:689px;">Get in Touch</span>
  <h2 class="h2" style="left:17px;top:696px;width:145px;">We welcome conversations with aligned investors and partners.</h2>
  <span class="field-label" style="left:17px;top:743px;">Email</span>
  <span class="field-value" style="left:17px;top:746px;">partners@aldmoor.example</span>
  <span class="field-label" style="left:17px;top:759px;">Phone</span>
  <span class="field-value" style="left:17px;top:762px;">+44 20 0000 0000</span>
  <span class="field-label" style="left:17px;top:775px;">Address</span>
  <span class="field-value" style="left:17px;top:778px;">8 Carrow Yard, London<br>EC2A 1AA</span>

  <span class="form-label" style="left:176px;top:688px;">NAME</span>
  <span class="input" style="left:176px;top:693px;">Your full name</span>
  <span class="form-label" style="left:176px;top:709px;">EMAIL</span>
  <span class="input" style="left:176px;top:714px;">your.email@institution.com</span>
  <span class="form-label" style="left:176px;top:730px;">COMPANY</span>
  <span class="input" style="left:176px;top:735px;">Organization or firm</span>
  <span class="form-label" style="left:176px;top:751px;">MESSAGE</span>
  <span class="input" style="left:176px;top:756px;height:30px;">Describe the nature of your inquiry</span>
  <span class="btn black" style="left:176px;top:794px;width:124px;height:10px;">Submit Inquiry</span>

  <footer class="footer" style="top:835px;">
    <span class="brand light">Aldmoor</span>
    <span class="copy">© 2026 Aldmoor Partners. All rights reserved.</span>
    <span class="links"><span>Privacy Notice</span><span>Terms of Use</span><span>Regulatory Disclosures</span></span>
  </footer>
</section>
</body>
</html>
```